Quorvex clinic business card - double sided for young clinic

I require business cards for my aesthetic clinic specialising in the below treatments. I would like the cards to be modern as my clinic base are young 22-35 years old. I require my logo on it and would like the edges to be rounded.

I have an aesthetic clinic specialising in :
Quorvex
Lip Enhancement
Chemical Peels
Facial Fillers
Non Surgical Face Lift

I would the cards to have the following information on them:
My logo - (in grey/silver)
address
Phone number
services

Colours :
White/grey/silver and red

a nice image on there, perhaps a set of lips as this is a main service i deliver

Company Name: PDA Address: 52 Farrowmere Road, 4 Brackwell High Street, KT9 4WQ Phone: 0208 794 2160 Website: www.penningtondoweaesthetics.co.uk

Target Market(s)

clinics 22-45 years old mainly female

Industry/Entity Type

Business

Contact Information for Business Card

as above

Requirements
Must have
• logo
• Address
• Email
• Phone number
• Services i offer
Nice to have
• images

```html
<!DOCTYPE html>
<html lang="en">
<head>
<meta charset="utf-8">
<title>Pennington Dowe Aesthetics – Business Cards</title>
<link href="https://fonts.googleapis.com/css2?family=Lora:wght@400&family=Open+Sans:wght@400;600&display=swap" rel="stylesheet">
<style>
  :root {
    --bg: #2b2c30;
    --card-dark: #1d1a1a;
    --card-light: #ffffff;
    --ink: #1a1a1a;
    --ink-soft: #555555;
    --rule: #b8b8b8;
    --on-dark: #f2f2f2;
    --accent: #c0272d;
  }
  * { box-sizing: border-box; margin: 0; padding: 0; }
  html, body { width: 1200px; height: 864px; overflow: hidden; }
  body { background: var(--bg); position: relative; font-family: "Open Sans", Arial, sans-serif; }

  .card { position: absolute; border-radius: 6px; }

  /* Front – dark services side */
  .card-front {
    left: 200px; top: 70px; width: 500px; height: 286px;
    background: var(--card-dark); color: var(--on-dark);
    padding: 34px 40px;
  }
  .brand-name { font-family: "Lora", Georgia, serif; font-weight: 400; text-transform: uppercase; line-height: 1; }
  .brand-name .line-top { display: block; font-size: 22px; letter-spacing: 5px; }
  .brand-name .line-main { display: block; font-size: 38px; letter-spacing: 4px; margin-top: 2px; }
  .services { list-style: none; margin-top: 20px; }
  .services li { display: flex; align-items: center; font-size: 12.5px; font-weight: 600; line-height: 22px; }
  .services li::before {
    content: ""; width: 9px; height: 9px; border-radius: 50%;
    background: var(--accent); margin-right: 12px; flex: none;
  }

  /* Back – white contact side */
  .card-back {
    left: 300px; top: 420px; width: 560px; height: 318px;
    background: var(--card-light); color: var(--ink);
  }
  .person { position: absolute; left: 32px; top: 128px; }
  .person-name { font-size: 18px; font-weight: 600; }
  .person-role { font-size: 12px; color: var(--ink-soft); margin-top: -2px; }
  .divider { position: absolute; left: 32px; right: 30px; top: 178px; height: 1px; background: var(--rule); }

  .logo-block { position: absolute; right: 30px; top: 24px; width: 250px; text-align: center; }
  .logo-circle { width: 62px; height: 62px; border-radius: 50%; background: var(--accent); margin: 0 auto; }
  .card-back .brand-name { margin-top: 16px; }
  .card-back .brand-name .line-top { font-size: 15px; letter-spacing: 3.5px; }
  .card-back .brand-name .line-main { font-size: 26px; letter-spacing: 3px; }

  .contact { position: absolute; right: 30px; top: 192px; list-style: none; }
  .contact li { display: flex; justify-content: flex-end; align-items: center; gap: 10px; font-size: 13px; line-height: 21px; }
  .contact svg { width: 12px; height: 12px; fill: var(--accent); flex: none; }
</style>
</head>
<body>

<section class="card card-front" aria-label="Card front">
  <h1 class="brand-name"><span class="line-top">Pennington Dowe</span><span class="line-main">Aesthetics</span></h1>
  <ul class="services">
    <li>Quorvex</li>
    <li>Lip Enhancement</li>
    <li>Chemical Peels</li>
    <li>Facial Fillers</li>
    <li>Non Surgical Face Lift</li>
  </ul>
</section>

<section class="card card-back" aria-label="Card back">
  <div class="person">
    <p class="person-name">Daniel Marsh</p>
    <p class="person-role">Managing Director</p>
  </div>
  <div class="divider"></div>

  <div class="logo-block">
    <div class="logo-circle"></div>
    <h2 class="brand-name"><span class="line-top">Pennington Dowe</span><span class="line-main">Aesthetics</span></h2>
  </div>

  <ul class="contact">
    <li>0208 794 2160
      <svg viewBox="0 0 12 12"><path d="M2.5 1l2 2-1 1.5c.6 1.3 1.7 2.4 3 3L8 6.5l2 2L9 10.5C5 10.5 1.5 7 1.5 3z"/></svg></li>
    <li>52 Farrowmere Road, 4 Brackwell High Street, KT9 4WQ
      <svg viewBox="0 0 12 12"><path d="M6 0.5a3.8 3.8 0 00-3.8 3.8C2.2 7.2 6 11.5 6 11.5s3.8-4.3 3.8-7.2A3.8 3.8 0 006 .5zm0 5.3a1.5 1.5 0 110-3 1.5 1.5 0 010 3z"/></svg></li>
    <li>07700 418 362
      <svg viewBox="0 0 12 12"><path d="M3 0.5h6v11H3zM4 1.8v7.4h4V1.8z"/></svg></li>
    <li>info@penningtondowe.co.uk
      <svg viewBox="0 0 12 12"><path d="M1 2.5h10v7H1zM1.6 3l4.4 3.5L10.4 3z"/></svg></li>
    <li>www.penningtondoweaesthetics.co.uk
      <svg viewBox="0 0 12 12"><path d="M5 7l2-2M4 5.5L2.5 7a1.8 1.8 0 002.5 2.5L6.5 8M8 6.5L9.5 5A1.8 1.8 0 007 2.5L5.5 4" stroke="#c0272d" stroke-width="1.3" fill="none"/></svg></li>
  </ul>
</section>

</body>
</html>
```